UI design for Fast Food Restaurant Self-Order App

Background:
App purpose: for fast food restaurant customers to self order food/drink by choosing item image, and make payment by tapping the credit card on the card terminal.
Reference: https://www.brivalotech.example/product-overview/self-order-kiosks/
Attachment:
Wireframes. (wire frames provide general idea and the information to display, they are not a strict guideline for layout design.)
Pollardo's Self ordering app.
Intro:
We have built a (for restaurant and cafe) Self Ordering and Payment app, similar to Pollardo's self ordering software in most of their new restaurants. Our app will be placed in a Quorvex Panes 10 OS touch screen Kiosk(screen size 4:3 or Portrait 16:9) within the restaurant/cafe premise.
Pages to be designed:
Page 1. Food Browsing Page. displays all food images(to be provided by cafes) by categories, and displays the Cart. This page will lead to Page 2 or Page 3.
'Cart' section should include:
'cart items/selected items', its quantity and price. like Pollardos' app.
When click on a Cart Item, we need to allow to change quantity or 'change Choice'. The UI handling these change requests with ease will be one deciding factor for us to choose your design.
Fact: up to 10 food categories, and 10 - 25 food items under each categories.
When click on one item image, it goes to Page 2.
Page 2. Item Detail/Description Page. Shows description of the food, and its available Choice(other food items or Special Request, up to 12) will also be displayed. 'Add item to cart' action(Button Name: ADD) will happen here and go back to Browsing Page 1.
e.g. Item 'Fried Rice' Page. the Choice could be 'Add Egg', 'Add Meat', 'No Chilli' etc.
Page 3. Order Review Page. No edit features allowed on this page, only two buttons: 'No' to go back to Browsing Page, or 'Yes' to proceed to Payment Page 4. Check Pollardo's screen.
Page 4. Payment Page - Prompt user to Insert or Tap credit card on the credit card terminal. (Exact wording: PLEASE FOLLOW INSTRUCTIONS DISPLAYED ON CREDIT CARD TERMINAL BELOW)
Page 5. Payment status. Successful / Failed.
Our considerations to pick the winner:
1. In terms of design for this task, we look out for page layout, effects, fonts, button style and overall colour scheme. the design should present itself in a clean and modern look, with minimum clicking or scrolling. The app aims to help customers choose and pay for their items quickly.
2.we need to handle both 4:3(as shown in wire frames) and 16:9 screens(like Pollardo's). there will be a lot more vertical space to utilise when it is in 16:9, resulting less scrolling than 4:3. tell us what you think.
All questions are welcome.
Winner has opportunity to work on a few more app UI. Cheers!
Industry/Entity Type
Fast Food Restaurant
Requirements
Must have
- Button colour differentiation - helps people know what to click next.
- best use of screen space. minimum click and scrolls.
Nice to have
- any personal touch.
Should not have
- unrelated design pattern, e.g. a cute animal or flower pattern in the layout.

```html
<!DOCTYPE html>
<html lang="en">
<head>
<meta charset="utf-8">
<title>Crustwell – Self Order Menu</title>
<link rel="stylesheet" href="https://fonts.googleapis.com/css2?family=Lexend:wght@300;400;500&display=swap">
<style>
  :root {
    --brand: #de5409;
    --ink: #2b2b2b;
    --rule: #cfcfcf;
    --panel: #ffffff;
    --side: #ffffff;
    --veg: #1f9d3a;
    --crust: #d9913f;
    --crust-light: #f2c977;
    --cheese: #f4dc9e;
  }
  * { box-sizing: border-box; margin: 0; padding: 0; }
  html, body {
    width: 1200px; height: 900px; overflow: hidden;
    background: var(--panel);
    font-family: "Lexend", "Helvetica Neue", sans-serif;
    color: var(--ink);
  }
  .kiosk { position: relative; width: 1200px; height: 900px; overflow: hidden; }

  /* Sidebar */
  .sidebar {
    position: absolute; left: 0; top: 0; width: 277px; height: 900px;
    background: var(--side);
    box-shadow: 2px 0 6px rgba(0,0,0,0.08);
    z-index: 2;
  }
  .brand-band {
    height: 125px; background: var(--brand);
    display: flex; align-items: center; padding-left: 34px;
  }
  .brand-name { color: #fff; font-weight: 500; font-size: 38px; letter-spacing: -0.5px; }
  .menu-title {
    font-size: 32px; font-weight: 500; line-height: 1;
    position: absolute; left: 35px; top: 170px;
  }
  .menu-rule { position: absolute; left: 10px; right: 23px; top: 228px; height: 1px; background: var(--rule); }
  .categories { list-style: none; position: absolute; left: 0; right: 0; top: 254px; }
  .category {
    position: relative; display: flex; align-items: center;
    height: 68px; padding-left: 38px; font-size: 24px; font-weight: 300;
  }
  .category svg { width: 36px; height: 36px; margin-right: 22px; flex: none; }
  .category.is-active { height: 64px; margin-bottom: 2px; background: var(--brand); color: #fff; font-weight: 500; }
  .category.is-active::after {
    content: ""; position: absolute; right: -17px; top: 0;
    border-top: 32px solid transparent; border-bottom: 32px solid transparent;
    border-left: 17px solid var(--brand);
  }

  /* Product grid */
  .product-grid {
    position: absolute; left: 277px; top: 0; width: 897px;
    display: grid; grid-template-columns: repeat(3, 288px);
    grid-template-rows: 382px 360px 160px;
    padding: 48px 0 0 47px;
  }
  .product { position: relative; }
  .product-photo {
    display: block; width: 160px; height: 160px; border-radius: 50%;
    margin-left: 28px;
    background: radial-gradient(circle, var(--cheese) 0 55%, var(--crust-light) 70%, var(--crust) 100%);
  }
  .product-photo.veggie {
    background:
      radial-gradient(circle at 35% 40%, #c8302a 0 4%, transparent 5%),
      radial-gradient(circle at 60% 30%, #3f8f2e 0 5%, transparent 6%),
      radial-gradient(circle at 65% 65%, #c8302a 0 4%, transparent 5%),
      radial-gradient(circle at 40% 70%, #e2b320 0 4%, transparent 5%),
      radial-gradient(circle, #efcf8a 0 60%, var(--crust-light) 72%, var(--crust) 100%);
  }
  .veg-mark {
    position: absolute; left: 26px; top: 153px; width: 11px; height: 11px;
    border: 1.5px solid var(--veg); display: grid; place-items: center;
  }
  .veg-mark::after { content: ""; width: 5px; height: 5px; border-radius: 50%; background: var(--veg); }
  .product-info {
    display: flex; justify-content: space-between; align-items: flex-start;
    width: 217px; margin-top: 39px;
  }
  .product-name { font-size: 19px; font-weight: 300; line-height: 26px; text-transform: uppercase; max-width: 160px; }
  .product-price { font-size: 26px; color: var(--brand); font-weight: 400; line-height: 26px; }
  .order-btn {
    display: block; margin: 47px 0 0 10px; width: 196px; height: 37px;
    border: 2px solid var(--brand); border-radius: 14px; background: #fff;
    color: var(--brand); font-family: inherit; font-size: 19px; font-weight: 300;
  }

  .cart-edge { position: absolute; right: 0; top: 0; width: 64px; height: 900px; z-index: 3; }
</style>
</head>
<body>
<main class="kiosk">
  <aside class="sidebar">
    <div class="brand-band"><span class="brand-name">Crustwell</span></div>
    <h1 class="menu-title">Menu</h1>
    <div class="menu-rule"></div>
    <ul class="categories">
      <li class="category is-active">
        <svg viewBox="0 0 36 36" fill="none" stroke="#fff" stroke-width="1.8"><path d="M6 32 L16 4 Q26 8 31 20 Z"/><path d="M12 22 Q20 20 24 26"/><circle cx="17" cy="14" r="2"/><circle cx="14" cy="26" r="2"/></svg>Pizza</li>
      <li class="category">
        <svg viewBox="0 0 36 36" fill="none" stroke="#777" stroke-width="1.6"><path d="M5 16 Q5 6 18 6 Q31 6 31 16 Z"/><path d="M4 20 H32"/><path d="M5 24 H31 V27 Q31 30 28 30 H8 Q5 30 5 27 Z"/></svg>Burgers</li>
      <li class="category">
        <svg viewBox="0 0 36 36" fill="none" stroke="#777" stroke-width="1.6"><path d="M4 16 H32 Q31 28 18 30 Q5 28 4 16 Z"/><path d="M9 16 Q10 8 15 10 Q18 5 22 10 Q27 8 27 16"/></svg>Salads</li>
      <li class="category">
        <svg viewBox="0 0 36 36" fill="none" stroke="#777" stroke-width="1.6"><path d="M4 26 Q4 10 18 10 Q32 10 32 26 Z"/><path d="M12 22 L16 16 M18 22 L22 16"/></svg>Tacos</li>
      <li class="category">
        <svg viewBox="0 0 36 36" fill="none" stroke="#777" stroke-width="1.6"><path d="M11 8 Q18 2 25 8 L23 32 H13 Z"/><path d="M11 8 Q18 14 25 8"/></svg>Wraps</li>
      <li class="category">
        <svg viewBox="0 0 36 36" fill="none" stroke="#777" stroke-width="1.6"><path d="M8 16 H28 L26 32 H10 Z"/><path d="M12 16 V5 M16 16 V3 M20 16 V4 M24 16 V6"/></svg>Fries</li>
      <li class="category">
        <svg viewBox="0 0 36 36" fill="none" stroke="#777" stroke-width="1.6"><path d="M8 10 H28 L25 32 H11 Z"/><path d="M7 10 H29"/><path d="M19 10 L22 3"/></svg>Drinks</li>
      <li class="category">
        <svg viewBox="0 0 36 36" fill="none" stroke="#777" stroke-width="1.6"><path d="M6 12 H13 Q12 6 17 6 Q22 6 21 12 H28 V19 Q34 18 34 23 Q34 28 28 27 V32 H6 Z"/></svg>Add-Ons</li>
    </ul>
  </aside>

  <section class="product-grid">
    <article class="product">
      <div class="product-photo veggie" role="img" aria-label="Pepper mix pizza photo"></div>
      <span class="veg-mark"></span>
      <div class="product-info"><span class="product-name">Pepper Mix</span><span class="product-price">$20</span></div>
      <button class="order-btn">Order Now</button>
    </article>
    <article class="product">
      <div class="product-photo veggie" role="img" aria-label="Green acre vegetable pizza photo"></div>
      <span class="veg-mark"></span>
      <div class="product-info"><span class="product-name">Green Acre</span><span class="product-price">$10</span></div>
    </article>
    <article class="product">
      <div class="product-photo" role="img" aria-label="Triple cheese pizza photo"></div>
      <span class="veg-mark"></span>
      <div class="product-info"><span class="product-name">Triple Cheese Classic</span><span class="product-price">$9</span></div>
    </article>
    <article class="product">
      <div class="product-photo veggie" role="img" aria-label="Spicy paneer pizza photo"></div>
      <span class="veg-mark"></span>
      <div class="product-info"><span class="product-name">Spicy Paneer</span><span class="product-price">$12</span></div>
    </article>
    <article class="product">
      <div class="product-photo veggie" role="img" aria-label="Zesty green salsa pizza photo"></div>
      <span class="veg-mark"></span>
      <div class="product-info"><span class="product-name">Zesty Green Salsa</span><span class="product-price">$13</span></div>
    </article>
    <article class="product">
      <div class="product-photo veggie" role="img" aria-label="Garden veggie pizza photo"></div>
      <span class="veg-mark"></span>
      <div class="product-info"><span class="product-name">Garden Veggie</span><span class="product-price">$12</span></div>
    </article>
    <article class="product">
      <div class="product-photo veggie" role="img" aria-label="Pepper pizza photo"></div>
    </article>
    <article class="product">
      <div class="product-photo veggie" role="img" aria-label="Vegetable pizza photo"></div>
    </article>
    <article class="product">
      <div class="product-photo" role="img" aria-label="Cheese pizza photo"></div>
    </article>
  </section>

  <svg class="cart-edge" viewBox="0 0 64 900" aria-label="Open cart">
    <line x1="38.5" y1="0" x2="38.5" y2="900" stroke="#e6e6e6" stroke-width="1"/>
    <path d="M38 0 H64 V148 L38 160 Z" fill="var(--brand)"/>
    <rect x="0" y="8" width="38" height="39" fill="var(--brand)"/>
    <path d="M23 18 V37 L13 27.5 Z" fill="#fff"/>
  </svg>
</main>
</body>
</html>
```